Talented energy healer needs business card design

I need a business card design for a new energy healing business in Perth Australia. As an energy healer I am quite earthy and practical rather than floaty and fairydust.
One of the techniques I use is unique in Australia but used internationally (US, UK and Europe). I practice with Coastal Pathway Therapy, Reiki and massage as well as some other techniques I developed personally. I am starting to incorporate sound healing into my practice. I literally change people's lives. The potential for each client is wide open. A key skill I bring to my practice is the capacity for making difficult situations seem more fun and less stressful.
Clients are likely to be depressed, physically unwell, going through a difficult time, unhappy with their current situation. They are people looking for new options to solve a difficult existing problem. They have probably tried other avenues before they come to me. They are open to something different.

I would like to communicate that the client and I work together for their healing and personal growth. I would like to convey that while the work of changing is challenging it can also be fun.

Hi all, info required on the card is:

Name
Title: Healer
contact number (mobile)
I don''t have a logo - I would be interested in seeing designs that use the whole card as well as the traditional logo on one side / in one corner. Whatever ''look/feel'' I choose will carry over to the website as well.

thanks
Meg

Reason: One or two of the designs caught my eye and many appeal for different reasons, but nothing is quite right for me. I've invited a couple of other designers to contribute so I wanted to give them time to be involved. kind regards Meg

Thank you all for the fabulous designs. I really appreciated the thought that many people put into my brief and a number of designs captured important things about what I was trying to say. It was a hard choice between 3 designs in the end.
thanks again and kind regards
Meg

Target Market(s)

people looking for new options to solve a difficult existing problem

Industry/Entity Type

Massage

Logo styles of interest
Abstract Logo
Requirements
Must have
• include green and blue
Nice to have
• hands, tea / teapots , the ocean, stepping stones

```html
<!DOCTYPE html>
<html lang="en">
<head>
<meta charset="utf-8">
<title>Meg – Energy Healer business card</title>
<link rel="stylesheet" href="https://fonts.googleapis.com/css2?family=Caveat:wght@500&family=Uncial+Antiqua&family=Oranienbaum&display=swap">
<style>
  :root {
    --backdrop: #a9b8b8;
    --card: #ffffff;
    --frame-green: #7df23a;
    --healer-blue: #2b4df2;
    --ink: #111111;
    --earth-dark: #3a1608;
    --earth-mid: #8a5634;
    --earth-light: #f1e6d2;
  }
  html, body {
    margin: 0;
    padding: 0;
    width: 1200px;
    height: 718px;
    overflow: hidden;
    background: var(--backdrop);
  }
  .canvas {
    position: relative;
    width: 1200px;
    height: 718px;
    background: var(--backdrop);
  }
  .card {
    position: absolute;
    left: 40px;
    top: 37px;
    width: 1118px;
    height: 641px;
    background: var(--card);
    border-radius: 100px;
  }
  .hands-frame {
    position: absolute;
    left: 116px;
    top: 109px;
    width: 488px;
    height: 335px;
  }
  .title {
    position: absolute;
    margin: 0;
    font-family: "Caveat", cursive;
    font-weight: 500;
    color: var(--healer-blue);
    font-size: 150px;
    line-height: 1;
    transform: skewX(-12deg) scaleX(1.15);
    transform-origin: left bottom;
    letter-spacing: 4px;
  }
  .title-energy { left: 638px; top: 170px; }
  .title-healer { left: 642px; top: 270px; }
  .name {
    position: absolute;
    left: 143px;
    top: 452px;
    margin: 0;
    font-family: "Uncial Antiqua", serif;
    font-size: 80px;
    line-height: 1;
    color: var(--ink);
    font-weight: 400;
  }
  .contact {
    position: absolute;
    left: 182px;
    top: 556px;
    margin: 0;
    font-family: "Oranienbaum", serif;
    font-size: 50px;
    line-height: 1;
    color: var(--ink);
    white-space: nowrap;
  }
  .contact .divider { margin: 0 30px 0 34px; }
</style>
</head>
<body>
<div class="canvas">
  <div class="card">
  </div>

  <svg class="hands-frame" viewBox="0 0 488 335" role="img" aria-label="Sepia photograph of two pairs of hands shaping clay together over a dark bowl">
    <defs>
      <linearGradient id="earth" x1="0" y1="0" x2="0.3" y2="1">
        <stop offset="0" stop-color="var(--earth-light)"/>
        <stop offset="0.45" stop-color="var(--earth-mid)"/>
        <stop offset="1" stop-color="var(--earth-dark)"/>
      </linearGradient>
    </defs>
    <rect x="2" y="2" width="484" height="331" rx="44" fill="none" stroke="var(--frame-green)" stroke-width="3"/>
    <rect x="8" y="8" width="472" height="319" rx="38" fill="none" stroke="var(--frame-green)" stroke-width="3"/>
    <rect x="13" y="12" width="463" height="311" rx="30" fill="url(#earth)"/>
  </svg>

  <h1 class="title title-energy">Energy</h1>
  <p class="title title-healer">Healer</p>

  <h2 class="name">Meg</h2>
  <p class="contact"><span class="phone">0412 555 036</span><span class="divider">~</span><span class="web">MendingWatersPath.com.au</span></p>
</div>
</body>
</html>
```